Business Card Design - ThriveMetric

Looking for creative, modern design, two sided for ThriveMetric that is consistent with color and feel of website www.thrivemetric.net.

Back of card will be used to promote products or have a quote revolving around decisions, change, leadership, innovation, creativity. Back should also have space to promote website, but optional to use the icon. Front of the card will need to use the icon and have standard place for name, job title, phone and email. We are not looking to put a mailing address or fax. Also want space to place a few words/phrase explaining what we do...such as individual growth and organizational development or tools, training, information...in addition, want the linkpage icon small on the front somewhere as we are also on linkpage.

Vector file uploaded of icon.

Target Market(s)

Professional coaching for individual growth and organizational development

Industry/Entity Type

Business

Requirements
Must have
• Icon...see attached.

```html
<!DOCTYPE html>
<html lang="en">
<head>
<meta charset="utf-8">
<title>ThriveMetric Business Card</title>
<link rel="stylesheet" href="https://fonts.googleapis.com/css2?family=Open+Sans:ital,wght@0,400;0,600;0,700;1,400&display=swap">
<style>
  :root {
    --backdrop: #d9dbdf;
    --card-white: #f1f3f7;
    --navy: #1d3673;
    --card-blue: #21519c;
    --card-blue-deep: #17407f;
    --accent-blue: #3f8fd8;
    --white: #ffffff;
    --soft-white: #dfe8f5;
  }
  * { margin: 0; padding: 0; box-sizing: border-box; }
  html, body {
    width: 1067px; height: 1200px; overflow: hidden;
    background: var(--backdrop);
    font-family: "Open Sans", Arial, sans-serif;
  }
  .canvas { position: relative; width: 1067px; height: 1200px; }
  .card {
    position: absolute; left: 183px; width: 700px; height: 400px;
    border-radius: 4px; overflow: hidden;
    box-shadow: 0 10px 30px rgba(0,0,0,0.25);
  }
  /* Back side */
  .card-back { top: 130px; background: var(--card-white); }
  .card-back .mark {
    position: absolute; left: 90px; top: 118px; width: 165px; height: 165px;
    border-radius: 50%; background: var(--accent-blue);
  }
  .card-back .brand {
    position: absolute; right: 60px; top: 150px; text-align: right;
    color: var(--navy);
  }
  .card-back .brand-name { font-size: 44px; font-weight: 400; line-height: 1; }
  .card-back .tagline { font-size: 28px; font-weight: 400; font-style: italic; margin-top: 10px; }
  .card-back .website { font-size: 17px; margin-top: 12px; }

  /* Front side */
  .card-front {
    top: 670px;
    background: linear-gradient(160deg, var(--card-blue) 0%, var(--card-blue-deep) 100%);
    color: var(--white);
  }
  .card-front .mark {
    position: absolute; left: 48px; top: 48px; width: 92px; height: 92px;
    border-radius: 50%; background: var(--accent-blue);
  }
  .card-front .brand { position: absolute; left: 160px; top: 60px; }
  .card-front .brand-name { font-size: 36px; font-weight: 400; line-height: 1; }
  .card-front .brand-line { font-size: 12.5px; font-weight: 400; color: var(--soft-white); margin-top: 6px; }
  .person { position: absolute; left: 48px; top: 255px; }
  .person-name { font-size: 24px; font-weight: 700; line-height: 1.1; }
  .person-title { font-size: 17px; color: var(--soft-white); }
  .social { display: flex; align-items: center; gap: 8px; margin-top: 14px; font-size: 18px; }
  .social-box { width: 18px; height: 18px; border-radius: 3px; background: var(--white); }
  .contact { position: absolute; left: 360px; top: 205px; list-style: none; }
  .contact li { display: flex; align-items: center; gap: 8px; font-size: 19px; line-height: 30px; }
  .contact svg { width: 20px; height: 20px; flex: none; }
</style>
</head>
<body>
<main class="canvas">
  <section class="card card-back" aria-label="Card back">
    <div class="mark" aria-hidden="true"></div>
    <div class="brand">
      <h1 class="brand-name">ThriveMetric</h1>
      <p class="tagline">“Grow With Purpose”</p>
      <p class="website">www.thrivemetric.net</p>
    </div>
  </section>

  <section class="card card-front" aria-label="Card front">
    <div class="mark" aria-hidden="true"></div>
    <div class="brand">
      <h2 class="brand-name">ThriveMetric</h2>
      <p class="brand-line">Empowering Personal Progress &amp; Collective Team Performance</p>
    </div>
    <div class="person">
      <p class="person-name">Daniel Harper</p>
      <p class="person-title">Position</p>
      <p class="social"><span class="social-box" aria-hidden="true"></span>/thrivemetric</p>
    </div>
    <ul class="contact">
      <li>
        <svg viewBox="0 0 20 20" aria-hidden="true"><rect width="20" height="20" rx="4" fill="#fff"/><path d="M6 4h3l1 4-2 1a8 8 0 0 0 3 3l1-2 4 1v3c0 1-1 2-2 2A11 11 0 0 1 4 6c0-1 1-2 2-2z" fill="#21519c"/></svg>
        1.800.555.0142
      </li>
      <li>
        <svg viewBox="0 0 20 20" aria-hidden="true"><rect width="20" height="20" rx="4" fill="#fff"/><rect x="4" y="6" width="12" height="8" fill="none" stroke="#21519c" stroke-width="1.6"/><path d="M4 6l6 5 6-5" fill="none" stroke="#21519c" stroke-width="1.6"/></svg>
        contact@thrivemetric.net
      </li>
      <li>
        <svg viewBox="0 0 20 20" aria-hidden="true"><rect width="20" height="20" rx="4" fill="#fff"/><circle cx="10" cy="10" r="6" fill="none" stroke="#21519c" stroke-width="1.5"/><path d="M4 10h12M10 4c-3 3-3 9 0 12M10 4c3 3 3 9 0 12" fill="none" stroke="#21519c" stroke-width="1.2"/></svg>
        www.thrivemetric.net
      </li>
    </ul>
  </section>
</main>
</body>
</html>
```